Keystone Ward Security - Trade Show Booth 10x20

I need designs for an upcoming trade show booth. We want something sleek, simple that represents our brand well.

Target Market(s)

property Managers

```html
<!DOCTYPE html>
<html lang="en">
<head>
<meta charset="utf-8">
<title>Keystone Ward Security – Trade Show Booth Banner</title>
<link href="https://fonts.googleapis.com/css2?family=Montserrat:ital,wght@0,700;0,800;1,700;1,800&display=swap" rel="stylesheet">
<style>
  :root {
    --backdrop: #c3c1c2;
    --paper: #ffffff;
    --ink: #000000;
    --brand-dark: #231f20;
    --signal-orange: #ff3d00;
    --photo-deep: #0a0c0f;
    --photo-charcoal: #1c1f23;
    --photo-slate: #2b3136;
    --photo-grey: #55595c;
    --photo-teal: #3a8fa3;
    --photo-teal-soft: #1f5363;
  }
  * { margin: 0; padding: 0; box-sizing: border-box; }
  html, body {
    width: 1200px; height: 708px; overflow: hidden;
    background: var(--backdrop);
    font-family: "Montserrat", Arial, sans-serif;
  }
  .banner {
    position: absolute; left: 79px; top: 93px;
    width: 1042px; height: 521px;
    background: var(--ink); overflow: hidden;
    box-shadow: 2px 3px 6px rgba(0,0,0,0.35);
  }
  .banner__photo {
    position: absolute; left: 400px; top: 0;
    width: 642px; height: 521px;
    background:
      linear-gradient(90deg, var(--ink) 0%, rgba(0,0,0,0.85) 14%, rgba(0,0,0,0) 42%),
      radial-gradient(ellipse 150px 55px at 70% 72%, var(--photo-grey), transparent 80%),
      radial-gradient(ellipse 210px 60px at 86% 34%, var(--photo-teal), transparent 75%),
      radial-gradient(ellipse 160px 70px at 62% 42%, var(--photo-teal-soft), transparent 80%),
      radial-gradient(ellipse 260px 240px at 68% 78%, var(--photo-charcoal), transparent 85%),
      linear-gradient(180deg, var(--photo-slate) 0%, var(--photo-slate) 45%, var(--photo-charcoal) 70%, var(--photo-deep) 100%);
  }
  .banner__header {
    position: absolute; left: 0; top: 0; width: 1042px; height: 221px;
  }
  .brand {
    position: absolute; left: 254px; top: 36px;
    display: flex; align-items: center; gap: 40px;
  }
  .brand__square {
    width: 94px; height: 94px; background: var(--brand-dark);
  }
  .brand__name {
    font-weight: 800; font-size: 34px; line-height: 1.08;
    letter-spacing: 2px; color: var(--brand-dark); text-transform: uppercase;
  }
  .pitch {
    position: absolute; left: 44px; top: 220px;
  }
  .pitch__eyebrow {
    font-style: italic; font-weight: 800; font-size: 19px;
    color: var(--paper); text-transform: uppercase;
  }
  .pitch__headline {
    margin-top: 12px;
    font-style: italic; font-weight: 800; font-size: 41px; line-height: 1.0;
    text-transform: uppercase; color: var(--paper);
  }
  .pitch__headline .accent { color: var(--signal-orange); display: block; }
  .phone {
    position: absolute; left: 44px; top: 366px;
    width: 444px; height: 63px; border-radius: 7px;
    background: var(--signal-orange); color: var(--ink);
    font-weight: 800; font-size: 60px; line-height: 63px;
    text-align: center; letter-spacing: 1px;
  }
  .website {
    position: absolute; left: 44px; top: 446px;
    font-style: italic; font-weight: 700; font-size: 23px;
    letter-spacing: 2.2px; color: var(--paper);
  }
</style>
</head>
<body>
  <div class="banner">
    <div class="banner__photo" role="img" aria-label="Photo of a security officer's black vest with a SECURITY patch in a dim control room with monitors"></div>

    <svg class="banner__header" viewBox="0 0 1042 221" aria-hidden="true">
      <polygon points="0,0 1042,0 1042,147 521,210 0,147" fill="var(--paper)"/>
      <polygon points="0,147 521,210 1042,147 1042,158 521,221 0,158" fill="var(--signal-orange)"/>
    </svg>

    <div class="brand">
      <div class="brand__square"></div>
      <div class="brand__name">Keystone Ward<br>Security</div>
    </div>

    <div class="pitch">
      <p class="pitch__eyebrow">Your partner in protection</p>
      <h1 class="pitch__headline"><span class="accent">Delivering scalable</span>Security solutions</h1>
    </div>

    <div class="phone">801-555-0142</div>
    <p class="website">www.keystonewardsecurity.com</p>
  </div>
</body>
</html>
```